Desk Allies Business Card

Contact Information for Business Card

Tauno Varjola
Managing Director

4/37 Brindle Street Larkvale ACT 2990

Tel: +61 02 6317 4826
Mob: +61 0427 653 194

Email: tauno@deskallies.com.au
Web: www.deskallies.com.au

Colors

Designer to choose colors to be used in the design.

Requirements
Must have
• Logo, Name, Title, Address, Telephone, Mobile, Email Address and Website
• "Desk Ally Global Pty Ltd"

```html
<!DOCTYPE html>
<html lang="en">
<head>
<meta charset="utf-8">
<title>Desk Allies Business Card</title>
<link rel="stylesheet" href="https://fonts.googleapis.com/css2?family=Lato:wght@400;700&display=swap">
<style>
  :root {
    --backdrop: #1c1c1c;
    --card-dark: #1a1a1a;
    --card-light: #efefef;
    --brand-blue: #1f72c0;
    --ink: #2b2b2b;
    --rule: #b5b5b5;
  }
  * { box-sizing: border-box; margin: 0; padding: 0; }
  html, body {
    width: 1200px; height: 900px; overflow: hidden;
    background: var(--backdrop);
    font-family: "Lato", sans-serif;
  }
  .stage {
    width: 1200px; height: 900px;
    display: flex; flex-direction: column;
    align-items: center; justify-content: center; gap: 50px;
  }
  .card {
    position: relative;
    width: 600px; height: 350px;
    border-radius: 26px;
    box-shadow: 0 10px 30px rgba(0,0,0,.5);
  }
  .card--back { background: var(--card-dark); }
  .card--front { background: var(--card-light); }

  .brand {
    position: absolute; left: 50%; transform: translateX(-50%);
    display: flex; align-items: center; gap: 12px; white-space: nowrap;
  }
  .brand__dot {
    width: 30px; height: 30px; border-radius: 50%;
    background: var(--brand-blue); flex: none;
  }
  .brand__name {
    font-weight: 700; font-size: 30px; letter-spacing: .5px;
    color: var(--brand-blue); line-height: 1;
  }
  .card--back .brand { top: 155px; }
  .card--back .site {
    position: absolute; right: 42px; bottom: 34px;
    font-size: 15px; color: var(--brand-blue);
  }

  .card--front .brand { top: 50px; }
  .address {
    position: absolute; right: 42px; top: 118px;
    text-align: right; font-style: normal;
    font-size: 16px; line-height: 1.3; color: var(--ink);
  }
  .person { position: absolute; left: 42px; top: 160px; }
  .person__name {
    font-weight: 700; font-size: 22px; color: var(--brand-blue);
    text-transform: uppercase; letter-spacing: .3px;
  }
  .person__role { font-size: 16px; color: var(--ink); margin-top: 2px; }
  .divider {
    position: absolute; left: 42px; right: 42px; top: 220px;
    border-top: 1px solid var(--rule);
  }
  .contacts {
    position: absolute; left: 42px; top: 232px;
    list-style: none; font-size: 16px; color: var(--ink); line-height: 24px;
  }
  .contacts li { display: flex; align-items: center; gap: 10px; }
  .contacts svg { width: 14px; height: 14px; fill: var(--brand-blue); flex: none; }
</style>
</head>
<body>
<main class="stage">
  <section class="card card--back" aria-label="Business card back">
    <div class="brand">
      <span class="brand__dot"></span>
      <span class="brand__name">DESK ALLIES</span>
    </div>
    <p class="site">www.deskallies.com.au</p>
  </section>

  <section class="card card--front" aria-label="Business card front">
    <div class="brand">
      <span class="brand__dot"></span>
      <span class="brand__name">DESK ALLIES</span>
    </div>
    <address class="address">
      Desk Ally<br>Global Pty Ltd<br>4/37 Brindle Street<br>Larkvale ACT 2990
    </address>
    <div class="person">
      <h1 class="person__name">Tauno Varjola</h1>
      <p class="person__role">Managing Director</p>
    </div>
    <div class="divider"></div>
    <ul class="contacts">
      <li><svg viewBox="0 0 16 16" aria-hidden="true"><path d="M1 5c0-2 2-3 7-3s7 1 7 3v1h-4V5H5v1H1zM3 8l2-2h6l2 2v6H3zm5 1.5a2 2 0 100 4 2 2 0 000-4z"/></svg>+61 02 6317 4826</li>
      <li><svg viewBox="0 0 16 16" aria-hidden="true"><path d="M4 1h8v14H4zm1.5 2v9h5V3zM8 12.7a.8.8 0 100 1.6.8.8 0 000-1.6z" fill-rule="evenodd"/></svg>+61 0427 653 194</li>
      <li><svg viewBox="0 0 16 16" aria-hidden="true"><path d="M1 3h14v10H1zm1.5 1.2V5l5.5 4 5.5-4v-.8z"/></svg>tauno@deskallies.com.au</li>
      <li><svg viewBox="0 0 16 16" aria-hidden="true"><circle cx="8" cy="8" r="7"/></svg>www.deskallies.com.au</li>
    </ul>
  </section>
</main>
</body>
</html>
```